deceased estate clean ups brochures

we would like a brochure to reresent our business we already have new web site and want to do DL A4 brochure to give out to promote our business we already have logo www.larkmore.com.au is where you can get all info needed

Target Market(s)

families with loved ones that have past away
people done sizing or needing to decluter

Colors
cadf82
33b8a4
886aae
33a6d7

```html
<!DOCTYPE html>
<html lang="en">
<head>
<meta charset="utf-8">
<title>Larkmore – Deceased Estate Cleanups Brochure</title>
<link href="https://fonts.googleapis.com/css2?family=Source+Sans+3:wght@400;600;700&display=swap" rel="stylesheet">
<style>
:root{
  --green:#4fae35;
  --green-dark:#3c972a;
  --green-deep:#2f8422;
  --green-light:#a6d66a;
  --lime:#cadf82;
  --head-green:#5aa733;
  --ink:#333;
  --ink-soft:#555;
  --paper:#fff;
  --bg:#c9c9c9;
}
*{box-sizing:border-box;margin:0;padding:0}
html,body{width:925px;height:1200px;overflow:hidden}
body{background:var(--bg);font-family:"Source Sans 3",Arial,sans-serif;color:var(--ink);position:relative}
.sheet{position:absolute;left:72px;width:780px;height:550px;background:var(--paper);display:flex;box-shadow:0 3px 8px rgba(0,0,0,.35);overflow:hidden}
.sheet--outside{top:40px}
.sheet--inside{top:620px}
.panel{position:relative;width:260px;height:100%;overflow:hidden}
.panel--green{background:linear-gradient(180deg,var(--green) 0%,var(--green-dark) 100%);color:#fff}
.abs{position:absolute}
.photo{position:absolute;left:0;width:100%}
.heading{font-weight:700;font-size:14px;color:var(--head-green);letter-spacing:.2px}
.heading--light{color:var(--lime)}
/* steps */
.steps{position:absolute;left:14px;right:12px;top:298px}
.step{display:flex;gap:5px;margin-bottom:9px}
.step__num{font-size:20px;line-height:18px;color:#444;font-weight:400}
.step__label{font-size:8px;font-weight:700;color:var(--green-dark);line-height:9px}
.step__text{font-size:7px;line-height:8px;color:var(--ink-soft)}
.step__text ul{padding-left:8px}
/* contact */
.logo-disc{position:absolute;left:56px;top:48px;width:148px;height:148px;border-radius:50%;background:#fff;display:flex;align-items:center;justify-content:center}
.brand{font-weight:700;color:var(--ink);letter-spacing:2px}
.contact__title{top:230px;width:100%;text-align:center;font-size:17px;font-weight:600}
.contact__intro{top:261px;left:25px;right:25px;text-align:center;font-size:10.5px;line-height:14px}
.socials{top:343px;width:100%;display:flex;justify-content:center;gap:14px}
.socials span{width:17px;height:17px;border:1.5px solid #fff;border-radius:50%}
.helpline{top:378px;width:100%;text-align:center;font-size:10px;color:var(--lime)}
.pill{position:absolute;background:var(--green-light);color:#fff;font-weight:600;border-radius:8px;display:flex;align-items:center;justify-content:center;gap:8px;letter-spacing:1.5px}
.contact__lines{top:443px;width:100%;text-align:center;font-size:11.5px;line-height:21px}
/* cover */
.cover__sub{top:460px;width:100%;text-align:center;font-size:10px;color:var(--green-dark)}
.cover__title{top:476px;width:100%;text-align:center;font-size:15.5px;font-weight:700;color:#333;letter-spacing:.3px}
.cover__text{top:502px;left:24px;right:24px;text-align:center;font-size:8.5px;line-height:11px;color:var(--ink-soft)}
/* about */
.about__text{left:13px;right:13px;top:303px;font-size:10.3px;line-height:13px}
.about__text p{margin-bottom:13px;text-align:justify}
/* services */
.service{position:absolute;left:18px;right:14px;display:flex;gap:9px}
.service__icon{flex:none;width:34px;height:34px;border-radius:50%;background:var(--green);box-shadow:0 0 0 2px #e6f2dc}
.service__title{font-size:8.5px;font-weight:600;color:#333}
.service__text{font-size:7px;line-height:8px;color:var(--ink-soft);text-align:justify}
.circle-photo{position:absolute;top:245px;width:78px;height:78px;border-radius:50%;border:2px solid #ddd}
/* why */
.why{position:absolute;left:12px;right:14px}
.why__label{display:flex;align-items:center;gap:5px;font-size:9px;color:var(--lime)}
.tick{width:11px;height:11px}
.why__text{font-size:7.5px;line-height:8.5px;padding-left:16px;margin-top:3px}
.rule{position:absolute;left:12px;right:14px;height:1px;background:rgba(255,255,255,.45)}
</style>
</head>
<body>

<!-- Outside sheet -->
<section class="sheet sheet--outside">

  <div class="panel panel--process">
    <div class="photo" style="top:0;height:256px;background:linear-gradient(135deg,#e9e6de 0%,#cfc7b6 45%,#7c8f6a 100%)" role="img" aria-label="Photo of cleaners in green uniforms wiping a table and mopping the floor"></div>
    <svg class="abs" style="top:0;left:0" width="260" height="50" viewBox="0 0 260 50"><path d="M0 0H260V10C180 12 90 20 0 48Z" fill="var(--green)"/><path d="M0 48C90 20 180 12 260 10V14C180 16 90 26 0 50Z" fill="#fff"/></svg>
    <h2 class="heading abs" style="left:14px;top:262px">OUR 5 STEP PROCESS</h2>
    <div class="steps">
      <div class="step"><div class="step__num">1</div><div><div class="step__label">STEP</div><div class="step__text">We start with a consultation at the property, understanding our client’s needs, requests and priorities. Create a plan of what needs to be done in each step of your move. Provide a personalized quote.</div></div></div>
      <div class="step"><div class="step__num">2</div><div><div class="step__label">STEP</div><div class="step__text">Pre-sale decluttering and sorting of items. Unwanted items to be sold, given to friends, family or charity.</div></div></div>
      <div class="step"><div class="step__num">3</div><div><div class="step__label">STEP</div><div class="step__text"><ul><li>We thoroughly clear and clean the property (inside and outside) prior to sale or rent.</li><li>House to be staged and set up to enhance its presentation for sale or rent.</li><li>Rubbish to be picked up.</li><li>Garden to be tidied.</li><li>After settlement, we begin to pack your possessions ready to be moved as directed.</li></ul></div></div></div>
      <div class="step"><div class="step__num">4</div><div><div class="step__label">STEP</div><div class="step__text">Organising and arranging transport of your possessions.</div></div></div>
      <div class="step"><div class="step__num">5</div><div><div class="step__label">STEP</div><div class="step__text">Storage or unpacking your possessions and setting up as per your instructions.</div></div></div>
    </div>
  </div>

  <div class="panel panel--green panel--contact">
    <div class="logo-disc"><span class="brand" style="font-size:17px">LARKMORE</span></div>
    <h2 class="contact__title abs">CONTACT US</h2>
    <p class="contact__intro abs">Welcome to Larkmore, a company that cares solely about your best interest and the care for the estate of your loved one.</p>
    <div class="socials abs"><span></span><span></span><span></span><span></span></div>
    <div class="helpline abs">WE’RE HERE TO HELP</div>
    <div class="pill" style="left:40px;top:406px;width:180px;height:24px;font-size:15px">
      <svg width="13" height="13" viewBox="0 0 24 24"><circle cx="12" cy="12" r="10.5" fill="none" stroke="#fff" stroke-width="2"/><path d="M8.5 6.5l2 2-1.2 1.5c.8 1.7 2 2.9 3.7 3.7l1.5-1.2 2 2-1.5 1.8c-4-.6-7.5-4.1-8.1-8.1z" fill="#fff"/></svg>
      0400 318 624
    </div>
    <div class="contact__lines abs">PO Box 220, Ashbury 3015<br>info@larkmore.com.au<br>www.larkmore.com.au</div>
  </div>

  <div class="panel panel--cover">
    <div class="abs" style="top:62px;width:100%;text-align:center"><span class="brand" style="font-size:22px">LARKMORE</span></div>
    <div class="photo" style="top:112px;height:335px;background:linear-gradient(160deg,#a8503c 0%,#c9b9a6 45%,#a7b6c9 100%)" role="img" aria-label="Photo of a smiling elderly couple sitting on a garden bench beside a bucket of cleaning supplies"></div>
    <svg class="abs" style="top:96px;left:0" width="260" height="36" viewBox="0 0 260 36"><path d="M0 16C90 30 180 10 260 0V36H0Z" fill="none"/><path d="M0 0H0C90 18 180 14 260 0V20C180 28 90 34 0 18Z" fill="#fff"/><path d="M30 24C120 30 200 16 260 4V12C200 24 120 32 30 24Z" fill="var(--green)"/></svg>
    <svg class="abs" style="top:420px;left:0" width="260" height="34" viewBox="0 0 260 34"><path d="M0 10C90 34 180 28 260 4V34H0Z" fill="#fff"/><path d="M0 8C90 30 180 24 260 0V5C180 28 90 34 0 14Z" fill="var(--green)"/></svg>
    <div class="cover__sub abs">WE’RE HERE TO HELP</div>
    <h1 class="cover__title abs">DECEASED ESTATE CLEANUPS</h1>
    <p class="cover__text abs">At Larkmore our goal is to ease your worries and help you with your journey in preparing your house for rental or resale.</p>
  </div>
</section>

<!-- Inside sheet -->
<section class="sheet sheet--inside">

  <div class="panel panel--about">
    <div class="photo" style="top:0;height:230px;background:linear-gradient(135deg,#d9d2c4 0%,#b7ab95 50%,#8c8d7c 100%)" role="img" aria-label="Photo of a consultant shaking hands with an elderly couple at home"></div>
    <div class="abs" style="top:215px;left:0;width:260px;height:335px;background:linear-gradient(180deg,var(--green),var(--green-dark))"></div>
    <svg class="abs" style="top:200px;left:0" width="260" height="40" viewBox="0 0 260 40"><path d="M0 40C70 22 160 10 260 8V0H0Z" fill="none"/><path d="M0 36C80 14 170 6 260 6V16C170 16 80 24 0 44Z" fill="#fff"/></svg>
    <h2 class="heading heading--light abs" style="left:13px;top:274px">ABOUT OUR COMPANY</h2>
    <div class="about__text abs" style="color:#fff">
      <p>At Larkmore our goal is to ease your worries and help you with your journey in preparing your house for rental or resale.</p>
      <p>Whether it is a move to another residence or the difficult task with dealing with the grief when a loved one passes away, Larkmore can help with the preparation of the property for sale. Larkmore will come in, remove unwanted items and dispose of all rubbish, do cosmetic repairs if required and leave the property in a spotless state.</p>
      <p>Our trained and reliable staff, repair any house and carry out landscaping in preparation for renting or resale of the property in a timely and professional manner. Our team provides a discrete and trust-worthy service, keeping in mind the sensitive nature of the work.</p>
    </div>
  </div>

  <div class="panel panel--services">
    <h2 class="heading abs" style="top:31px;width:100%;text-align:center">SERVICES OFFERED</h2>
    <div class="service" style="top:70px"><div class="service__icon"></div><div><div class="service__title">Senior / Aged Care Relocations and Down sizing</div><div class="service__text">If you’re relocating into age care or downsizing your living arrangements, Larkmore offers you a complete service to assist you in moving to your new home.</div></div></div>
    <div class="service" style="top:122px"><div class="service__icon"></div><div><div class="service__title">Deceased Estates</div><div class="service__text">Losing a love one and being left with the task of finalizing and clearing out a property, can be difficult and traumatic for families to deal with. Let our professional team help you.</div></div></div>
    <div class="service" style="top:180px"><div class="service__icon"></div><div><div class="service__title">Cleaning Service</div><div class="service__text">We can provide a Cleaning Service for a house sale or rental preparation or a deceased estate. Let us make these decisions easier for you.</div></div></div>
    <div class="circle-photo" style="left:22px;background:linear-gradient(135deg,#c8c1b4,#8f8677)" role="img" aria-label="Photo of movers loading boxes into a truck"></div>
    <div class="circle-photo" style="left:91px;background:linear-gradient(135deg,#b9c4cf,#6e6a63)" role="img" aria-label="Photo of a house exterior with a ladder during repairs"></div>
    <div class="circle-photo" style="left:160px;background:linear-gradient(135deg,#e2d8c8,#a3907a)" role="img" aria-label="Photo of a couple carrying furniture into a new home"></div>
    <div class="service" style="top:350px"><div class="service__icon"></div><div><div class="service__title">Cosmetic Repairs and House Maintenance</div><div class="service__text">At Larkmore, we are experienced in Cosmetic Repairs, House Maintenance and house renovations and we can help you achieve the maximum return on the renting or sale of your property.</div></div></div>
    <div class="service" style="top:408px"><div class="service__icon"></div><div><div class="service__title">Preparation for Rental or Sale</div><div class="service__text">Our target is to create maximum appeal on all aspects of your property, allowing you to sell or rent and attract a higher sale price when properly prepared and presented.</div></div></div>
    <div class="service" style="top:460px"><div class="service__icon"></div><div><div class="service__title">Garden Makeovers</div><div class="service__text">We run a successful landscaping business, The Fernleaf Group Garden Division, offering a full service in landscaping and construction...</div></div></div>
    <div class="pill" style="left:52px;top:517px;width:156px;height:18px;font-size:12.5px;background:var(--lime)">
      <svg width="11" height="11" viewBox="0 0 24 24"><circle cx="12" cy="12" r="10.5" fill="none" stroke="#fff" stroke-width="2"/><path d="M8.5 6.5l2 2-1.2 1.5c.8 1.7 2 2.9 3.7 3.7l1.5-1.2 2 2-1.5 1.8c-4-.6-7.5-4.1-8.1-8.1z" fill="#fff"/></svg>
      0400 318 624
    </div>
  </div>

  <div class="panel panel--why">
    <div class="abs" style="top:0;left:0;width:260px;height:345px;background:linear-gradient(180deg,var(--green),var(--green-dark))"></div>
    <div class="photo" style="top:330px;height:220px;background:linear-gradient(135deg,#f1efe9 0%,#d6d3cb 55%,#8d96a3 100%)" role="img" aria-label="Photo of cleaners in overalls wiping a table and mopping the floor"></div>
    <svg class="abs" style="top:306px;left:0" width="260" height="50" viewBox="0 0 260 50"><path d="M0 22C90 38 180 30 260 4V20C180 44 90 50 0 38Z" fill="#fff"/><path d="M0 38C90 50 180 44 260 20V26C180 50 90 54 0 44Z" fill="var(--green-light)"/></svg>
    <h2 class="heading heading--light abs" style="left:12px;top:31px">WHY CHOOSE US?</h2>
    <div class="why" style="top:63px"><div class="why__label"><svg class="tick" viewBox="0 0 12 12"><circle cx="6" cy="6" r="5" fill="none" stroke="var(--lime)"/><path d="M3.5 6l1.8 1.8L8.6 4.3" fill="none" stroke="var(--lime)" stroke-width="1.2"/></svg>Quality</div><div class="why__text">Our goal is to enhance your property and achieve the results you are looking for. We appreciate the trust placed in us to deliver a quality job that meets your expectations…</div></div>
    <div class="rule" style="top:116px"></div>
    <div class="why" style="top:124px"><div class="why__label"><svg class="tick" viewBox="0 0 12 12"><circle cx="6" cy="6" r="5" fill="none" stroke="var(--lime)"/><path d="M3.5 6l1.8 1.8L8.6 4.3" fill="none" stroke="var(--lime)" stroke-width="1.2"/></svg>Professionalism</div><div class="why__text">Larkmore only use quality staff and materials that are “fit for purpose”. We keep a professional approach to every job ensuring all agreed tasks are completed and accounted…</div></div>
    <div class="rule" style="top:178px"></div>
    <div class="why" style="top:185px"><div class="why__label"><svg class="tick" viewBox="0 0 12 12"><circle cx="6" cy="6" r="5" fill="none" stroke="var(--lime)"/><path d="M3.5 6l1.8 1.8L8.6 4.3" fill="none" stroke="var(--lime)" stroke-width="1.2"/></svg>Pride</div><div class="why__text">We take pride in our family approach and care we bring to your loved ones belongings. Whether it is simple house clearing, house repairs or larger renovations your…</div></div>
    <div class="rule" style="top:238px"></div>
    <div class="why" style="top:246px"><div class="why__label"><svg class="tick" viewBox="0 0 12 12"><circle cx="6" cy="6" r="5" fill="none" stroke="var(--lime)"/><path d="M3.5 6l1.8 1.8L8.6 4.3" fill="none" stroke="var(--lime)" stroke-width="1.2"/></svg>Areas Serviced</div><div class="why__text">Specialising in Melbourne CBD and suburbs including: Coburg, Falkner, Campbellfield, Craigieburn, St. Kilda, Brighton, Caulfield, Hawthorn, Heidelberg, Watsonia…</div></div>
  </div>
</section>

</body>
</html>
```